Cosmetics Brand Logo and Bottle Label Design

We are creating a new cosmetics brand called "Nolan Whitby" and would like you to create an amazing logo and bottle label for this brand's new 100% pure argan oil product.
For the logo, we really like the logo's of Marin Calloway and Vessa. The text should be Sans Serif (without feet).
For the actual bottle label, please find attached labels of one of our competitors design which really like. We really like the simplicity and elegance of the design. The only difference is that our product will be using light turqoise as the brand color. Please feel free to add your own creativity into it as well.
Industry/Entity Type
Cosmetics
Logo Text
Nolan Whitby
Font styles to use

```html
<!DOCTYPE html>
<html lang="en">
<head>
<meta charset="utf-8">
<title>Nolan Whitby – Argan Oil Label</title>
<link rel="stylesheet" href="https://fonts.googleapis.com/css2?family=Montserrat:wght@300;400&display=swap">
<style>
  :root {
    --backdrop: #ececec;
    --label-teal: #7ed8cc;
    --band-teal: #52d6c5;
    --foot-teal: #9fe3da;
    --gold-dark: #c08f62;
    --gold-light: #e3b98f;
    --gold-line: #cfa37a;
    --ink-white: #ffffff;
    --ink-soft: rgba(255,255,255,0.85);
  }
  * { margin: 0; padding: 0; box-sizing: border-box; }
  html, body {
    width: 1022px; height: 1200px; overflow: hidden;
    background: var(--backdrop);
    font-family: "Montserrat", Arial, sans-serif;
  }
  .label {
    position: absolute; left: 81px; top: 54px;
    width: 860px; height: 1092px;
    background: var(--label-teal);
    color: var(--ink-white);
  }
  .brand-frame {
    position: absolute; left: 31px; top: 121px;
    width: 787px; height: 246px;
    border: 3px solid var(--gold-line);
    padding: 12px;
  }
  .brand-plate {
    width: 100%; height: 100%;
    background: linear-gradient(90deg, var(--gold-dark), var(--gold-light) 65%, var(--gold-dark));
    display: flex; align-items: center; justify-content: center;
  }
  .brand-name {
    font-weight: 300; font-size: 88px; letter-spacing: 2px;
    color: var(--ink-white); text-transform: lowercase;
  }
  .divider-rule {
    position: absolute; top: 455px; height: 3px;
    background: var(--gold-line);
  }
  .divider-rule.left { left: 31px; width: 315px; }
  .divider-rule.right { left: 500px; width: 318px; }
  .drop-icon { position: absolute; left: 414px; top: 425px; width: 24px; height: 36px; }
  .product-name {
    position: absolute; left: 0; right: 0; top: 520px;
    text-align: center; font-weight: 400; font-size: 86px;
    letter-spacing: 10px; color: var(--ink-white);
  }
  .info-band {
    position: absolute; left: 0; right: 0; top: 704px; height: 330px;
    background: var(--band-teal);
  }
  .foot-strip {
    position: absolute; left: 0; right: 0; top: 1034px; height: 58px;
    background: var(--foot-teal);
  }
  .tagline {
    position: absolute; left: 0; right: 0; top: 88px;
    text-align: center; font-weight: 300; font-size: 32px;
    letter-spacing: 3px; color: var(--ink-soft);
  }
  .tag-rule {
    position: absolute; left: 37px; width: 777px; top: 143px; height: 3px;
    background: rgba(255,255,255,0.8);
  }
  .spec-divider {
    position: absolute; left: 426px; top: 147px; width: 3px; height: 161px;
    background: var(--ink-white);
  }
  .spec {
    position: absolute; top: 170px; text-align: center;
    font-weight: 300; color: var(--ink-white);
  }
  .spec.volume { left: 60px; width: 340px; font-size: 36px; line-height: 58px; }
  .spec.purity { left: 440px; width: 400px; }
  .purity-figure { font-size: 54px; line-height: 60px; letter-spacing: 4px; }
  .purity-note { font-size: 34px; letter-spacing: 3px; color: var(--ink-soft); }
</style>
</head>
<body>
  <main class="label">
    <div class="brand-frame">
      <div class="brand-plate">
        <span class="brand-name">nolan whitby</span>
      </div>
    </div>

    <div class="divider-rule left"></div>
    <svg class="drop-icon" viewBox="0 0 24 36" aria-hidden="true">
      <path d="M12 2 C12 2 3 18 3 24 a9 9 0 0 0 18 0 C21 18 12 2 12 2 Z" fill="var(--gold-line)"/>
    </svg>
    <div class="divider-rule right"></div>

    <h1 class="product-name">ARGAN OIL</h1>

    <section class="info-band">
      <p class="tagline">light weight &amp; moiturizing oil</p>
      <div class="tag-rule"></div>
      <div class="spec volume">120 ml/<br>4fl oz</div>
      <div class="spec-divider"></div>
      <div class="spec purity">
        <div class="purity-figure">100 %</div>
        <div class="purity-note">pure natural</div>
      </div>
    </section>
    <div class="foot-strip"></div>
  </main>
</body>
</html>
```